Glow & Gloss by Mina
Text 410.582.3107 to set up and appointment
Instagram is Glow_GlossByMina
Location 4318 Fernwick Rd. Ashmere Md, 21087 Suit 204
Slogan "Radiant Shine. Timeless You.
Specializing in pressicion cuts, blonding, fades, perms, waxing and more

The salon is black, gun metal color mirror with led lights. Green plants and has natural wood countertops for accent colors. Modern yet elegant. I want the card simple but it needs something to really grab the clients attention. I like black, grey, gold, green, natural tones and hints of pink or gold coloring
I’m open to anything. I don’t have a logo. Suggestions are welcome

Target Market(s)

20-60 men and woman

Industry/Entity Type

Hairstylist / barber

Contact Information for Business Card

The name of the show should be bold. Maybe the letters could raised I also like foil for shine added or a mat finish

Colors

Designer to choose colors to be used in the design.

Requirements
Must have
• I also like some floral Floral designs, but not too overpowering. I like Sparkle, Watercolor design, Or a geometric line in the background
Nice to have
• I’m really here because I need creative help. I’m open for suggestions. I’ll post a picture of the salon in inspiration if I can find it.
Should not have
• Checkered background

```html
<!DOCTYPE html>
<html lang="en">
<head>
<meta charset="utf-8">
<title>Glow &amp; Gloss by Mina – Business Card</title>
<link rel="stylesheet" href="https://fonts.googleapis.com/css2?family=Questrial&family=Montserrat:wght@700;800&display=swap">
<style>
  :root {
    --stage: #2a2a2b;
    --sage: #a1a27a;
    --gold: #e9a93a;
    --gold-light: #f6cf6e;
    --silver: #e4e4dc;
    --cream: #e8e2d8;
    --olive: #a3a47b;
    --ink: #1d1d1b;
    --accent-pink: #d9346a;
  }
  * { box-sizing: border-box; margin: 0; padding: 0; }
  html, body { width: 1200px; height: 875px; overflow: hidden; }
  body {
    background: var(--stage);
    font-family: "Questrial", sans-serif;
    display: flex;
    align-items: center;
    justify-content: center;
    gap: 40px;
  }
  .card {
    position: relative;
    width: 540px;
    height: 309px;
    border-radius: 18px;
    overflow: hidden;
  }
  .card__frame {
    position: absolute;
    inset: 16px;
    border-radius: 14px;
  }

  /* Front */
  .card--front { background: var(--sage); }
  .card--front .card__frame {
    border: 2px solid var(--gold);
    box-shadow: 0 0 0 0.5px var(--gold-light) inset;
  }
  .front__brand {
    position: absolute;
    left: 0; right: 0; top: 100px;
    text-align: center;
    font-size: 44px;
    letter-spacing: 1px;
    color: var(--silver);
  }
  .front__slogan {
    position: absolute;
    left: 0; right: 0; top: 228px;
    text-align: center;
    font-size: 16px;
    letter-spacing: 0.5px;
    color: #fbfaf4;
  }

  /* Back */
  .card--back { background: var(--cream); color: var(--ink); }
  .card--back .card__frame { border: 2px solid var(--olive); }
  .back__content {
    position: absolute;
    inset: 0;
    display: flex;
    flex-direction: column;
    align-items: center;
    padding-top: 30px;
    text-align: center;
  }
  .back__brand {
    font-size: 30px;
    color: var(--olive);
    letter-spacing: 0.5px;
  }
  .back__name {
    margin-top: 4px;
    font-family: "Montserrat", sans-serif;
    font-weight: 800;
    font-size: 21px;
    color: var(--olive);
    letter-spacing: 0.3px;
  }
  .back__address {
    margin-top: 8px;
    font-size: 13.5px;
    line-height: 1.3;
  }
  .back__note {
    margin-top: 6px;
    font-size: 13.5px;
  }
  .back__phone {
    margin-top: 6px;
    font-family: "Montserrat", sans-serif;
    font-weight: 700;
    font-size: 19px;
    letter-spacing: 0.5px;
  }
  .back__social {
    margin-top: 5px;
    display: flex;
    align-items: center;
    gap: 6px;
    font-size: 12.5px;
  }
  .back__social-dot {
    width: 12px; height: 12px;
    border-radius: 50%;
    background: var(--accent-pink);
  }
  .back__services {
    margin-top: 7px;
    font-size: 13.5px;
    line-height: 1.35;
  }
</style>
</head>
<body>
  <section class="card card--front" aria-label="Card front">
    <div class="card__frame"></div>
    <p class="front__brand">Glow &amp; Gloss by Mina</p>
    <p class="front__slogan">Radiant Shine. Timeless You</p>
  </section>

  <section class="card card--back" aria-label="Card back">
    <div class="card__frame"></div>
    <div class="back__content">
      <p class="back__brand">Glow &amp; Gloss by Mina</p>
      <p class="back__name">Mina Calloway</p>
      <p class="back__address">4318 Fernwick Rd. Ashmere Md<br>21087 Suit 204</p>
      <p class="back__note">please text to schedule your appointment</p>
      <p class="back__phone">410.582.3107</p>
      <p class="back__social"><span class="back__social-dot"></span>Glow_GlossByMina</p>
      <p class="back__services">Pressicion cuts &bull; Blonding &bull; Fades &bull; Perms<br>waxing and more</p>
    </div>
  </section>
</body>
</html>
```